Real Estate Website

I am looking for a website design for a website that will be featuring real estate listings across Australia. It will be a website for a real estate agency that operates through all states in Australia.

We like the designs of https://www.brightharbourhomes.com.au/ and https://velmora.asia/

On the lifestyle website, we like the sell, buy, sold tabs but would also like lease, and agents. We also need a button somewhere for 'Join Agent Pallisto' and 'Login'

On the Velmora site it has a concierge section and we want something like that on the home page.

The contact details to show in the footer are:

Shop 2174B
Level 1 Tidewater Plaza Shopping Centre
87 Quarry Lane
Southport

Attached are various versions of the logo and some intro text to go on the home page.

```html
<!DOCTYPE html>
<html lang="en">
<head>
<meta charset="utf-8">
<title>Agent Pallisto — Real Estate Properties</title>
<link href="https://fonts.googleapis.com/css2?family=Forum&family=Allura&family=Inter:wght@400;500;600&display=swap" rel="stylesheet">
<style>
:root{
  --gold:#a8892e;
  --gold-light:#c9ad5c;
  --page:#faf9f6;
  --ink:#1d1d1b;
  --muted:#6d6d68;
  --panel:#161a17;
  --deep:#1b2b31;
  --line:#e6e3dc;
  --white:#ffffff;
}
*{margin:0;padding:0;box-sizing:border-box}
html,body{width:1200px;height:4854px;overflow:hidden}
body{background:var(--page);font-family:"Inter",sans-serif;color:var(--ink);position:relative}
.block{position:absolute;left:0;width:1200px}
.serif{font-family:"Forum",serif;font-weight:400}
.script{font-family:"Allura",cursive;color:var(--gold);position:absolute;white-space:nowrap}

/* hero */
.hero{top:0;height:438px;border-radius:0 0 44px 44px;overflow:hidden;
  background:linear-gradient(180deg,#3b3a2c 0%,#5a5a3a 35%,#6d6a3f 60%,#3d4027 100%)}
.hero-nav{position:absolute;top:28px;left:60px;right:60px;display:flex;justify-content:space-between;font-size:11px;color:var(--white)}
.hero-nav ul{list-style:none;display:flex;gap:9px}
.hero-nav li+li:before{content:"|";margin-right:9px}
.brand{position:absolute;top:40px;left:0;width:1200px;text-align:center;font-size:11px;letter-spacing:2px;color:var(--gold-light);text-transform:uppercase}
.brand-dot{display:inline-block;width:8px;height:8px;border-radius:50%;background:var(--gold-light);margin-right:6px;vertical-align:1px}
.hero-title{position:absolute;top:160px;width:1200px;text-align:center;font-size:36px;color:var(--white)}
.search{position:absolute;top:243px;left:297px;width:605px;height:31px;background:var(--white);border-radius:16px;display:flex;align-items:center;font-size:9px;color:var(--muted)}
.search span{padding-left:14px}
.search .s-loc{width:236px}
.search .s-sel{width:125px;display:flex;justify-content:space-between;padding-right:12px}
.search-btn{position:absolute;right:0;top:0;height:31px;width:120px;background:var(--gold);border-radius:16px;color:var(--white);display:flex;align-items:center;justify-content:center;gap:5px;font-size:9px}
.stats{position:absolute;top:305px;width:1200px;display:flex;justify-content:center;gap:18px;font-size:8px;color:var(--white)}
.stats span:before{content:"";display:inline-block;width:5px;height:5px;border-radius:50%;background:var(--gold-light);margin-right:8px;vertical-align:1px}

/* section headings */
.heading{position:absolute;width:1200px;text-align:center;font-size:30px;color:var(--ink)}
.sub{position:absolute;width:1200px;text-align:center;font-size:10px;line-height:18px;color:var(--muted)}

/* listings */
.cats{position:absolute;top:574px;left:280px;width:640px;display:flex;justify-content:space-between;font-size:9px;color:#555}
.cat{display:flex;flex-direction:column;align-items:center;gap:5px}
.cat svg{width:14px;height:14px}
.listing-grid{position:absolute;left:117px;width:966px;display:grid;grid-template-columns:repeat(4,230px);column-gap:15px}
.listing-photo{position:relative;height:248px;border-radius:4px}
.badge{position:absolute;top:10px;font-size:7px;color:var(--white);padding:2px 7px;border-radius:8px;background:#2a2a26}
.badge.gold{background:var(--gold)}
.b-left{left:10px}
.b-r1{right:46px}.b-r2{right:10px}
.avatar{position:absolute;left:10px;bottom:12px;width:28px;height:28px;border-radius:50%;background:#c9b8a3;border:2px solid var(--white)}
.heart{position:absolute;right:10px;bottom:12px;width:14px;height:14px}
.listing-info{padding-top:10px;height:80px}
.price{font-size:10px;color:var(--gold)}
.l-title{font-size:10px;font-weight:500;margin-top:5px}
.specs{font-size:8px;color:#444;margin-top:5px}
.btn-gold{position:absolute;background:var(--gold);color:var(--white);font-size:9px;display:flex;align-items:center;justify-content:center;border-radius:4px}

/* passionate */
.passion{top:1353px;height:529px;background:linear-gradient(90deg,#b9b7b3 0%,#d7d5d1 35%,#c9c5bf 70%,#8e7e6b 100%)}
.passion-title{position:absolute;top:100px;width:1200px;text-align:center;font-size:32px;line-height:38px;color:var(--white)}
.service-row{position:absolute;top:215px;left:242px;display:flex;gap:13px}
.service{width:230px;height:212px;background:var(--white);border-radius:3px;display:flex;flex-direction:column;align-items:center;padding-top:40px;text-align:center}
.service-icon{width:36px;height:36px;border-radius:50%;background:var(--gold);display:flex;align-items:center;justify-content:center}
.service h3{font-size:11px;font-weight:500;margin-top:14px}
.service p{font-size:8px;line-height:14px;color:var(--muted);margin-top:10px;width:170px}
.service a{font-size:8px;color:var(--gold);margin-top:12px;text-decoration:none}

/* concierge */
.concierge-photo{position:absolute;top:1952px;left:98px;width:425px;height:466px;border-radius:22px 0 0 22px;background:linear-gradient(160deg,#8a6c52 0%,#c7b8a2 40%,#e9e6e0 70%,#6a5e52 100%)}
.concierge-panel{position:absolute;top:2028px;left:523px;width:579px;height:327px;background:var(--panel);border-radius:0 30px 30px 0;padding:48px 0 0 75px}
.concierge-panel h2{font-size:28px;color:var(--gold);font-family:"Inter",sans-serif;font-weight:500}
.concierge-panel .q{font-size:14px;line-height:23px;color:var(--white);margin-top:20px}
.concierge-panel .d{font-size:10px;line-height:22px;color:var(--gold);margin-top:18px;width:440px}
.concierge-panel .btn-gold{position:static;width:119px;height:24px;margin-top:18px}

/* featured properties */
.feat-grid{position:absolute;top:2648px;left:98px;display:grid;grid-template-columns:repeat(3,329px);gap:11px 9px}
.feat-card{background:var(--white);border:1px solid var(--line);box-shadow:0 2px 6px rgba(0,0,0,.05)}
.feat-photo{position:relative;height:152px}
.feat-price{position:absolute;left:10px;bottom:8px;background:var(--gold);color:var(--white);font-size:7px;padding:2px 7px;border-radius:8px}
.feat-badge{position:absolute;right:10px;top:10px;background:var(--gold);color:var(--white);font-size:6px;padding:2px 7px;border-radius:8px}
.feat-info{height:53px;display:flex;align-items:center;padding-left:14px;gap:10px}
.feat-avatar{width:26px;height:26px;border-radius:50%;background:#c7b5a0}
.feat-info b{display:block;font-size:10px;font-weight:500}
.feat-info span{font-size:8px;color:var(--muted)}

/* agents */
.agents{position:absolute;top:3285px;left:93px;display:flex;gap:14px}
.agent{width:237px;height:281px}

/* neighbourhoods */
.hood{position:absolute;overflow:hidden;color:var(--white);display:flex;flex-direction:column;align-items:center;justify-content:flex-end;padding-bottom:14px}
.hood b{font-family:"Forum",serif;font-weight:400;font-size:15px}
.hood span{font-size:8px;margin-top:4px}

/* digital */
.digital{top:4162px;height:438px;background:var(--deep)}
.digital h2{position:absolute;top:108px;left:110px;font-size:31px;line-height:36px;color:var(--white)}
.digital p{position:absolute;top:236px;left:110px;width:390px;font-size:9px;line-height:17px;color:#d9dee0}
.digital-actions{position:absolute;top:295px;left:110px;display:flex;align-items:center;gap:12px;font-size:8px;color:var(--white)}
.pill{border:1px solid var(--white);border-radius:12px;padding:7px 16px;letter-spacing:1px}
.digital-img1{position:absolute;top:28px;left:602px;width:249px;height:280px;border-radius:16px 16px 0 16px}
.digital-img2{position:absolute;top:238px;left:862px;width:241px;height:155px}

/* footer */
.footer{top:4600px;height:254px}
.foot-brand{position:absolute;top:78px;left:107px;font-size:10px;letter-spacing:2px;color:var(--gold);text-transform:uppercase}
.foot-note{position:absolute;top:104px;left:107px;width:380px;font-size:9px;line-height:15px;color:#333}
.foot-col{position:absolute;top:56px;font-size:8px;line-height:13px;color:#333}
.foot-col h4{font-family:"Forum",serif;font-weight:400;font-size:12px;margin-bottom:18px}
.foot-rule{position:absolute;top:200px;left:107px;width:986px;height:1px;background:var(--line)}
.copy{position:absolute;top:212px;left:107px;font-size:7px;color:#333}
.socials{position:absolute;top:212px;left:970px;display:flex;gap:8px}
.socials i{width:18px;height:18px;border:1px solid #333;border-radius:50%}
</style>
</head>
<body>

<header class="block hero" role="img" aria-label="Vineyard hills with a hilltop village at dusk">
  <nav class="hero-nav">
    <ul><li>Listings</li><li>Locations</li><li>Featured</li><li>Concierge</li></ul>
    <ul><li>Projects</li><li>Contact Us</li><li>Join Agent Pallisto</li><li>Login</li></ul>
  </nav>
  <div class="brand"><span class="brand-dot"></span>Agent Pallisto</div>
  <h1 class="hero-title serif">Real Estate Properties</h1>
  <span class="script" style="top:185px;left:722px;font-size:26px">Explore</span>
  <div class="search">
    <span class="s-loc">Search by location</span>
    <span class="s-sel">Property Type <em>⌄</em></span>
    <span class="s-sel">Sell or Rent <em>⌄</em></span>
    <div class="search-btn">
      <svg width="9" height="9" viewBox="0 0 10 10" fill="none" stroke="#fff" stroke-width="1.4"><circle cx="4" cy="4" r="3"/><path d="M6.3 6.3 9 9"/></svg>SEARCH
    </div>
  </div>
  <div class="stats"><span>7,000+ SOLD HOMES</span><span>1 BILLION $ IN SALES</span><span>1,000+ SATISFIED CUSTOMERS</span></div>
</header>

<section class="listings">
  <h2 class="heading serif" style="top:502px">Best Listings Available</h2>
  <span class="script" style="top:523px;left:693px;font-size:22px">finest</span>
  <div class="cats">
    <div class="cat"><svg viewBox="0 0 14 14" fill="none" stroke="#555"><path d="M2 7 7 2l5 5M3.5 6v6h7V6"/></svg>For Sale</div>
    <div class="cat"><svg viewBox="0 0 14 14" fill="none" stroke="#555"><path d="M2 7 7 2l5 5M3.5 6v6h7V6M6 12V9h2v3"/></svg>For Rent</div>
    <div class="cat"><svg viewBox="0 0 14 14" fill="none" stroke="#555"><path d="M2 6 7 2l5 4v6H2z"/></svg>Residential</div>
    <div class="cat"><svg viewBox="0 0 14 14" fill="none" stroke="#555"><rect x="3" y="2" width="8" height="10"/><path d="M5 5h4M5 8h4"/></svg>Apartments</div>
    <div class="cat"><svg viewBox="0 0 14 14" fill="none" stroke="#555"><path d="M2 7 7 3l5 4v5H2z"/></svg>Single Homes</div>
    <div class="cat"><svg viewBox="0 0 14 14" fill="none" stroke="#555"><rect x="3" y="2" width="8" height="10"/></svg>Studios</div>
    <div class="cat"><svg viewBox="0 0 14 14" fill="none" stroke="#555"><path d="M2 7 7 2l5 5v5H2z"/></svg>Condos</div>
    <div class="cat"><svg viewBox="0 0 14 14" fill="none" stroke="#555"><rect x="2" y="4" width="10" height="8"/><path d="M5 4V2h4v2"/></svg>Commercial</div>
    <div class="cat"><svg viewBox="0 0 14 14" fill="none" stroke="#555"><path d="M2 5h10l-1 7H3zM4 5l1-3h4l1 3"/></svg>Shops</div>
  </div>

  <div class="listing-grid" style="top:632px">
    <article>
      <div class="listing-photo" role="img" aria-label="Stone villa below snowy mountains" style="background:linear-gradient(180deg,#7e8fa8,#a4877a 55%,#6e5a48)">
        <span class="badge b-left">Featured</span><span class="badge gold b-r1">For Sale</span><span class="badge gold b-r2">Sold</span>
        <span class="avatar"></span>
        <svg class="heart" viewBox="0 0 14 14" fill="none" stroke="#fff" stroke-width="1.2"><path d="M7 12S2 8.7 2 5.2A2.5 2.5 0 0 1 7 4a2.5 2.5 0 0 1 5 1.2C12 8.7 7 12 7 12z"/></svg>
      </div>
      <div class="listing-info"><div class="price">$ 5,500,000</div><div class="l-title">Villa With Panoramic View</div><div class="specs">Bedrooms: 5 &nbsp; Bathrooms: 3 &nbsp; Size: 250 ft²</div></div>
    </article>
    <article>
      <div class="listing-photo" role="img" aria-label="Modern two-storey townhouse lit at dusk" style="background:linear-gradient(180deg,#8a939b,#5a4a3a 55%,#3a3a36)">
        <span class="badge b-left">Featured</span><span class="badge gold b-r1">For Sale</span><span class="badge gold b-r2">Sold</span>
        <span class="avatar"></span>
        <svg class="heart" viewBox="0 0 14 14" fill="none" stroke="#fff" stroke-width="1.2"><path d="M7 12S2 8.7 2 5.2A2.5 2.5 0 0 1 7 4a2.5 2.5 0 0 1 5 1.2C12 8.7 7 12 7 12z"/></svg>
      </div>
      <div class="listing-info"><div class="price">$ 210,000</div><div class="l-title">Townhouse For Sale</div><div class="specs">Bedrooms: 3 &nbsp; Bathrooms: 3 &nbsp; Size: 190 ft²</div></div>
    </article>
    <article>
      <div class="listing-photo" role="img" aria-label="Timber-clad family house with lawn" style="background:linear-gradient(180deg,#c9d2d8,#8a6a4c 55%,#5f7a3e)">
        <span class="badge b-left">Featured</span><span class="badge gold b-r1">For Sale</span><span class="badge gold b-r2">Sold</span>
        <span class="avatar"></span>
        <svg class="heart" viewBox="0 0 14 14" fill="none" stroke="#fff" stroke-width="1.2"><path d="M7 12S2 8.7 2 5.2A2.5 2.5 0 0 1 7 4a2.5 2.5 0 0 1 5 1.2C12 8.7 7 12 7 12z"/></svg>
      </div>
      <div class="listing-info"><div class="price">$ 100,000</div><div class="l-title">Family House For Sale</div><div class="specs">Bedrooms: 2 &nbsp; Bathrooms: 5 &nbsp; Size: 29,000 ft²</div></div>
    </article>
    <article>
      <div class="listing-photo" role="img" aria-label="Grand Mediterranean mansion with hedges" style="background:linear-gradient(180deg,#8fb0cc,#c9a45e 55%,#4f6a32)">
        <span class="badge b-left">Featured</span><span class="badge gold b-r1">For Sale</span><span class="badge gold b-r2">Active</span>
        <span class="avatar"></span>
        <svg class="heart" viewBox="0 0 14 14" fill="none" stroke="#fff" stroke-width="1.2"><path d="M7 12S2 8.7 2 5.2A2.5 2.5 0 0 1 7 4a2.5 2.5 0 0 1 5 1.2C12 8.7 7 12 7 12z"/></svg>
      </div>
      <div class="listing-info"><div class="price">$ 770,000</div><div class="l-title">Gorgeous Studio For Rent</div><div class="specs">Bedrooms: 5 &nbsp; Bathrooms: 6 &nbsp; Size: 190 ft²</div></div>
    </article>
  </div>

  <div class="listing-grid" style="top:962px">
    <article>
      <div class="listing-photo" role="img" aria-label="Tuscan-style family home with green lawn" style="background:linear-gradient(180deg,#a9c4dc,#c7a780 50%,#5c8a36)">
        <span class="badge gold b-r1">For Rent</span><span class="badge gold b-r2">Sold</span>
        <span class="avatar"></span>
        <svg class="heart" viewBox="0 0 14 14" fill="none" stroke="#fff" stroke-width="1.2"><path d="M7 12S2 8.7 2 5.2A2.5 2.5 0 0 1 7 4a2.5 2.5 0 0 1 5 1.2C12 8.7 7 12 7 12z"/></svg>
      </div>
      <div class="listing-info"><div class="price">$ 5,500,000</div><div class="l-title">Awesome Family Apartment</div><div class="specs">Bedrooms: 3 &nbsp; Bathrooms: 2.5 &nbsp; Size: 1,200 ft²</div></div>
    </article>
    <article>
      <div class="listing-photo" role="img" aria-label="Modern home among trees" style="background:linear-gradient(180deg,#9fb6c6,#a89a82 50%,#3f5a2a)">
        <span class="badge gold b-r1">For Sale</span><span class="badge gold b-r2">Sold</span>
        <span class="avatar"></span>
        <svg class="heart" viewBox="0 0 14 14" fill="none" stroke="#fff" stroke-width="1.2"><path d="M7 12S2 8.7 2 5.2A2.5 2.5 0 0 1 7 4a2.5 2.5 0 0 1 5 1.2C12 8.7 7 12 7 12z"/></svg>
      </div>
      <div class="listing-info"><div class="price">$ 775,000</div><div class="l-title">Modern Home For Sale</div><div class="specs">Bedrooms: 5 &nbsp; Bathrooms: 6 &nbsp; Size: 190 ft²</div></div>
    </article>
    <article>
      <div class="listing-photo" role="img" aria-label="Stone apartment building with arched entry" style="background:linear-gradient(180deg,#b8c6d2,#8a7560 50%,#5a4a3c)">
        <span class="badge gold b-r1">For Rent</span><span class="badge gold b-r2">Active</span>
        <span class="avatar"></span>
        <svg class="heart" viewBox="0 0 14 14" fill="none" stroke="#fff" stroke-width="1.2"><path d="M7 12S2 8.7 2 5.2A2.5 2.5 0 0 1 7 4a2.5 2.5 0 0 1 5 1.2C12 8.7 7 12 7 12z"/></svg>
      </div>
      <div class="listing-info"><div class="price">$ 800 <small>/ month</small></div><div class="l-title">Apartment Space For Rent</div><div class="specs">Bedrooms: 5 &nbsp; Bathrooms: 4 &nbsp; Size: 500 ft²</div></div>
    </article>
    <article>
      <div class="listing-photo" role="img" aria-label="Home with turquoise pool at night" style="background:linear-gradient(180deg,#2c4a6a,#c29a5a 45%,#1f9ab0)">
        <span class="badge gold b-r1">For Sale</span><span class="badge gold b-r2">Sold</span>
        <span class="avatar"></span>
        <svg class="heart" viewBox="0 0 14 14" fill="none" stroke="#fff" stroke-width="1.2"><path d="M7 12S2 8.7 2 5.2A2.5 2.5 0 0 1 7 4a2.5 2.5 0 0 1 5 1.2C12 8.7 7 12 7 12z"/></svg>
      </div>
      <div class="listing-info"><div class="price">$ 800,000</div><div class="l-title">Spacious Home For Sale</div><div class="specs">Bedrooms: 2 &nbsp; Bathrooms: 4 &nbsp; Size: 500 ft²</div></div>
    </article>
  </div>
  <div class="btn-gold" style="top:1292px;left:540px;width:120px;height:24px;border-radius:6px">Load More Listings</div>
</section>

<section class="block passion" role="img" aria-label="Bright living room interior with sofa and lanterns">
  <h2 class="passion-title serif">Passionate About<br>Being Different</h2>
  <span class="script" style="top:152px;left:655px;font-size:26px">experience</span>
  <div class="service-row">
    <div class="service">
      <div class="service-icon"><svg width="16" height="16" viewBox="0 0 16 16" fill="none" stroke="#fff" stroke-width="1.2"><path d="M2 8 8 3l6 5M4 7v6h8V7"/></svg></div>
      <h3>Sell Your Home</h3><p>We do a free evaluation to be sure you want to start selling.</p><a>Read More →</a>
    </div>
    <div class="service">
      <div class="service-icon"><svg width="16" height="16" viewBox="0 0 16 16" fill="none" stroke="#fff" stroke-width="1.2"><path d="M8 13S3 10 3 6.3A2.6 2.6 0 0 1 8 5a2.6 2.6 0 0 1 5 1.3C13 10 8 13 8 13z"/></svg></div>
      <h3>Buy A Home</h3><p>We do a free evaluation to be sure you want to start selling.</p><a>Read More →</a>
    </div>
    <div class="service">
      <div class="service-icon"><svg width="16" height="16" viewBox="0 0 16 16" fill="none" stroke="#fff" stroke-width="1.2"><rect x="4" y="3" width="8" height="10"/><path d="M6 6h4M6 9h4"/></svg></div>
      <h3>Rent A Home</h3><p>We do a free evaluation to be sure you want to start selling.</p><a>Read More →</a>
    </div>
  </div>
</section>

<section class="concierge">
  <div class="concierge-photo" role="img" aria-label="Portrait of a real estate agent in front of a home"></div>
  <div class="concierge-panel">
    <h2>Agent Pallisto Concierge</h2>
    <p class="q">Looking buy, rent or sell something unique?<br>Want competitive developer financing at great rates?</p>
    <p class="d">Concierge can help you find, buy, rent or sell unique properties through our extensive global agent network and assist with financing at competitive rates with fast approvals.</p>
    <div class="btn-gold">Find out more</div>
  </div>
</section>

<section class="featured">
  <h2 class="heading serif" style="top:2512px">Featured Properties</h2>
  <span class="script" style="top:2534px;left:663px;font-size:20px">Napa Valley</span>
  <p class="sub" style="top:2568px">With unparalleled attention to detail, superior craftsmanship, and desirable amenities, each Featured<br>Property embodies the epitome of luxury living.</p>
  <div class="feat-grid">
    <div class="feat-card"><div class="feat-photo" role="img" aria-label="Hillside villa above green valley" style="background:linear-gradient(180deg,#9fb4c4,#a08a6a 50%,#4e6a30)"><span class="feat-badge">Active</span><span class="feat-price">$ 2,200 / month</span></div><div class="feat-info"><span class="feat-avatar"></span><div><b>Modern Penthouse Apartment</b><span>2 Beds · 2.5 Baths · 250 ft2</span></div></div></div>
    <div class="feat-card"><div class="feat-photo" role="img" aria-label="Colonial home with wide verandas" style="background:linear-gradient(180deg,#b8c8d6,#c8b89c 50%,#5a7a36)"><span class="feat-badge">Sold</span><span class="feat-price">$ 775,000</span></div><div class="feat-info"><span class="feat-avatar"></span><div><b>Modern Home For Sale</b><span>2 Beds · 2.5 Baths · 250 ft2</span></div></div></div>
    <div class="feat-card"><div class="feat-photo" role="img" aria-label="Home with pool at twilight" style="background:linear-gradient(180deg,#2c4a6a,#b8925a 50%,#2c8aa0)"><span class="feat-badge">Sold</span><span class="feat-price">$ 800,000</span></div><div class="feat-info"><span class="feat-avatar"></span><div><b>Spacious Home For Sale</b><span>2 Beds · 2.5 Baths · 250 ft2</span></div></div></div>
    <div class="feat-card"><div class="feat-photo" role="img" aria-label="Modern townhouse at dusk" style="background:linear-gradient(180deg,#8a939b,#5a4a3a 55%,#3a3a36)"><span class="feat-badge">Sold</span><span class="feat-price">$ 210,000</span></div><div class="feat-info"><span class="feat-avatar"></span><div><b>Townhouse For Sale</b><span>2 Beds · 2.5 Baths · 250 ft2</span></div></div></div>
    <div class="feat-card"><div class="feat-photo" role="img" aria-label="Aerial view of villa among trees" style="background:linear-gradient(180deg,#5f7a46,#7e8a5a 50%,#3e5a2a)"><span class="feat-badge">Active</span><span class="feat-price">$ 450,000</span></div><div class="feat-info"><span class="feat-avatar"></span><div><b>Luxury Villa For Sale</b><span>2 Beds · 2.5 Baths · 250 ft2</span></div></div></div>
    <div class="feat-card"><div class="feat-photo" role="img" aria-label="Large house behind green garden" style="background:linear-gradient(180deg,#a9bccb,#b6a58a 45%,#4a7030)"><span class="feat-badge">Open House</span><span class="feat-price">$ 1,800 / month</span></div><div class="feat-info"><span class="feat-avatar"></span><div><b>Modern Office For Rent</b><span>2 Beds · 2.5 Baths · 250 ft2</span></div></div></div>
  </div>
</section>

<section class="team">
  <h2 class="heading serif" style="top:3144px">Meet Our Agents</h2>
  <span class="script" style="top:3165px;left:600px;font-size:20px">professionals</span>
  <p class="sub" style="top:3201px">In the vibrant neighborhood of San Jose, California, Lena is renowned among residents, property developers,<br>local businesses, and professionals in the real estate industry.</p>
  <div class="agents">
    <div class="agent" role="img" aria-label="Agent portrait outside a house" style="background:linear-gradient(180deg,#8a7b6a,#b4aea4 60%,#6e6a62)"></div>
    <div class="agent" role="img" aria-label="Agent portrait holding a tablet" style="background:linear-gradient(180deg,#7a5a44,#c2b3a0 60%,#2f3440)"></div>
    <div class="agent" role="img" aria-label="Agent portrait in a suit" style="background:linear-gradient(180deg,#b5bcc4,#a8453a 40%,#2a2c30)"></div>
    <div class="agent" role="img" aria-label="Agent portrait in a bright office" style="background:linear-gradient(180deg,#dcd7cf,#c8b7a3 60%,#e2ddd4)"></div>
  </div>
</section>

<section class="neighbourhoods">
  <h2 class="heading serif" style="top:3669px">Featured Neighborhoods</h2>
  <span class="script" style="top:3690px;left:672px;font-size:20px">Napa Valley</span>
  <p class="sub" style="top:3724px">In the vibrant neighborhood of San Jose, California, Lena is renowned among residents, property<br>developers, local businesses, and professionals in the real estate industry.</p>
  <div class="hood" role="img" aria-label="Commercial building at dusk" style="top:3790px;left:9px;width:188px;height:165px;background:linear-gradient(180deg,#5a6a80,#8a6a4e 60%,#3a3a30)"><b>Commercial</b><span>0 Listings</span></div>
  <div class="hood" role="img" aria-label="Residential houses" style="top:3790px;left:207px;width:201px;height:165px;background:linear-gradient(180deg,#8fa6bd,#8a7a66 60%,#4a5a36)"><b>Residential</b><span>1 Listing</span></div>
  <div class="hood" role="img" aria-label="Vineyard valley with mountains" style="top:3790px;left:417px;width:376px;height:342px;background:linear-gradient(180deg,#6a7a84,#5a6a4a 45%,#3a4a2a)"><b>Multi Family House</b><span>0 Listings</span></div>
  <div class="hood" role="img" aria-label="Apartments among vineyards" style="top:3790px;left:805px;width:188px;height:165px;background:linear-gradient(180deg,#8a9aa6,#7a8a5a 50%,#3e5a2a)"><b>Apartments</b><span>3 Listings</span></div>
  <div class="hood" role="img" aria-label="Modern glass studio building" style="top:3790px;left:1002px;width:188px;height:165px;background:linear-gradient(180deg,#6a7a8a,#8a6a4a 50%,#2e3a2a)"><b>Studio</b><span>0 Listings</span></div>
  <div class="hood" role="img" aria-label="Condos at sunset" style="top:3965px;left:9px;width:188px;height:167px;background:linear-gradient(180deg,#c99a6a,#6a5a4a 55%,#3a3a2e)"><b>Condos</b><span>3 Listings</span></div>
  <div class="hood" role="img" aria-label="Duplex homes" style="top:3965px;left:207px;width:201px;height:167px;background:linear-gradient(180deg,#a0b2c4,#9a8672 55%,#4a5a3a)"><b>Duplexes</b><span>1 Listing</span></div>
  <div class="hood" role="img" aria-label="Houses on green hills" style="top:3965px;left:805px;width:188px;height:167px;background:linear-gradient(180deg,#7a8ea0,#5a7a4a 50%,#2e4a22)"><b>Houses</b><span>1 Listing</span></div>
  <div class="hood" role="img" aria-label="Office tower at night" style="top:3965px;left:1002px;width:188px;height:167px;background:linear-gradient(180deg,#2a3a5a,#6a4a3a 55%,#1e2430)"><b>Office</b><span>0 Listings</span></div>
</section>

<section class="block digital">
  <h2 class="serif">Your digital presence is<br>about to take off</h2>
  <span class="script" style="top:152px;left:310px;font-size:22px">Napa Valley</span>
  <p>Welcome to our blog, your go-to destination for all things real estate and beyond. Join us as we explore the exciting world of real estate together and unlock the keys to your dream home.</p>
  <div class="digital-actions"><span class="pill">CONTACT US</span>OR<span class="pill">SEARCH LISTINGS</span></div>
  <div class="digital-img1" role="img" aria-label="Estate home surrounded by vineyards" style="background:linear-gradient(180deg,#6a7a82,#7a6a4e 45%,#3e5a2a)"></div>
  <div class="digital-img2" role="img" aria-label="Aerial view of estate with gardens" style="background:linear-gradient(180deg,#5a7a8a,#5a6a3a 50%,#2a3a1e)"></div>
</section>

<footer class="block footer">
  <div class="foot-brand">Agent Pallisto</div>
  <p class="foot-note">All information is deemed reliable but not guaranteed and should be independently reviewed and verified.</p>
  <div class="foot-col" style="left:510px"><h4>Visit Us</h4>Shop 2174B<br>Level 1 Tidewater Plaza Shopping Centre<br>87 Quarry Lane<br>Southport</div>
  <div class="foot-col" style="left:712px"><h4>Working Hours</h4>Monday – Friday<br>09:00 am – 09:00 pm<br>Saturday – Sunday – Closed</div>
  <div class="foot-col" style="left:915px"><h4>Quick Links</h4>About<br><br>Contact<br><br>List with Us</div>
  <div class="foot-rule"></div>
  <div class="copy">© All rights reserved.</div>
  <div class="socials"><i></i><i></i><i></i><i></i><i></i></div>
</footer>

</body>
</html>
```